Lower-middle market private equity firm needs its PowerPoint template update/refresh

Brackwell Thorne Equity Partners is a lower-middle market private equity firm focused on acquiring family- and founder-owned businesses in the industrial market. Website is here for more info: https://www.bteqx.com/. We would like to upgrade/update our powerpoint template/slide master we use for marketing materials - uploading a powerpoint version with some of the slide templates we use. We would like to keep it classic and clean with a white background and color on top and enough room for text on the pages. We would prefer to stay within the color palette of the hash tag logo on the cover page (cover page needs an update as well). We are open to suggestions on the font we utilize as well.

```html
<!DOCTYPE html>
<html lang="en">
<head>
<meta charset="utf-8">
<title>Brackwell Thorne Equity Partners – Presentation Template</title>
<link href="https://fonts.googleapis.com/css2?family=Montserrat:wght@600;700;800;900&family=Lato:wght@400;700&display=swap" rel="stylesheet">
<style>
:root{
  --page:#d9d9d9;
  --blue:#2f6d9c;
  --green:#337d55;
  --sky:#4a95d2;
  --olive:#b7a532;
  --navy:#1b3a57;
  --taupe:#8a7f78;
  --stone:#857a72;
  --panel:#efebe7;
  --panel-grey:#e8e6e4;
  --ink:#4a4a4a;
  --body:#444;
  --muted:#7a7a7a;
  --rule:#a9bdb1;
}
*{box-sizing:border-box;margin:0;padding:0}
html,body{width:776px;height:1200px;overflow:hidden;background:var(--page)}
body{position:relative;font-family:'Lato',sans-serif;color:var(--body)}

/* sheet header */
.sheet-brand{position:absolute;left:29px;top:40px;display:flex;align-items:center;gap:10px}
.brand-square{width:44px;height:44px;background:var(--sky)}
.brand-name{font:800 21px/1.05 'Montserrat',sans-serif;color:var(--stone);text-transform:uppercase;width:185px}
.sheet-divider{position:absolute;left:249px;top:30px;width:1.5px;height:67px;background:#333}
.sheet-heading{position:absolute;left:269px;top:32px;font:900 19.5px/23.5px 'Montserrat',sans-serif;letter-spacing:2.4px;color:var(--blue)}

/* slide frame */
.slide{position:absolute;width:352px;height:198px;background:#fff;box-shadow:0 1px 3px rgba(0,0,0,.3);overflow:hidden}
.col-l{left:29px}.col-r{left:396px}
.row1{top:130px}.row2{top:341px}.row3{top:553px}.row4{top:764px}.row5{top:975px}
.slide-title{position:absolute;left:10px;top:6px;font:700 9.5px 'Montserrat',sans-serif;color:#555}
.title-rule{position:absolute;left:10px;right:10px;top:21px;height:.7px;background:var(--rule)}
.corner-mark{position:absolute;right:10px;top:8px;display:flex;align-items:center;gap:2px;font:700 4px 'Lato',sans-serif;color:var(--stone)}
.corner-mark i{display:block;width:7px;height:7px;background:var(--sky)}
.foot{position:absolute;bottom:5px;font-size:4px;color:var(--muted)}
.foot-l{left:11px}.foot-r{right:11px}
.footnote{position:absolute;left:11px;bottom:14px;font-size:3.6px;color:var(--muted)}

/* bullets */
.bl{position:relative;padding-left:6px}
.bl::before{content:"›";position:absolute;left:0;top:-1px;font:700 6px 'Lato',sans-serif;color:var(--olive)}
.bl b{display:block;font:400 6.4px/1.15 'Lato',sans-serif;color:var(--blue)}
.bl span{display:block;font-size:4.6px;line-height:1.2;color:var(--body)}
.line{position:relative;padding-left:6px;font-size:4.6px;line-height:1.2;color:var(--body)}
.line::before{content:"›";position:absolute;left:0;top:-1px;font:700 5.5px 'Lato',sans-serif;color:var(--olive)}

/* section boxes */
.box{position:absolute;background:var(--panel);border-radius:4px;overflow:hidden}
.box-head{height:18px;padding-left:7px;font:400 6.5px/18px 'Lato',sans-serif;color:#fff}
.box-body{padding:6px 8px;display:flex;flex-direction:column;gap:8px}
.bg-blue{background:var(--blue)}.bg-green{background:var(--green)}.bg-sky{background:var(--sky)}.bg-olive{background:var(--olive)}

/* slide 1 */
.cover-brand{position:absolute;left:11px;top:36px;display:flex;align-items:center;gap:4px}
.cover-brand i{display:block;width:20px;height:20px;background:var(--sky)}
.cover-brand span{font:800 7.6px/1.05 'Montserrat',sans-serif;color:var(--stone);text-transform:uppercase;width:70px}
.cover-headline{position:absolute;left:10px;top:68px;font:800 15.4px/19.5px 'Montserrat',sans-serif;color:var(--ink);text-transform:uppercase}
.values{position:absolute;left:11px;top:111px;display:flex;gap:5px}
.values span{width:67px;height:13px;border-radius:1.5px;font:700 5.6px/13px 'Lato',sans-serif;color:#fff;text-align:center}
.cover-rule{position:absolute;left:10px;right:10px;top:133px;height:.6px;background:#ddd}
.cover-url{position:absolute;left:12px;top:139px;font-size:6.5px;color:#222}
.cover-date{position:absolute;left:11px;top:153px;font-size:6.5px;color:#222}

/* slide 2 */
.two-col{position:absolute;left:11px;top:45px;right:10px;display:grid;grid-template-columns:1fr 1fr;row-gap:7.5px;column-gap:10px}

/* slide 3 */
.team-bar{position:absolute;left:11px;width:176px;height:13px;border-radius:2px;padding-left:7px;font:400 6.2px/13px 'Lato',sans-serif;color:#fff}
.team-grid{position:absolute;left:11px;width:176px;display:grid;grid-template-columns:repeat(3,1fr);row-gap:5px}
.member{text-align:center;font-size:4px;line-height:1.25;color:#333}
.member .foto{width:20px;height:20px;border-radius:50%;background:#4a4a4a;margin:0 auto 3px;font-size:4px;line-height:20px;color:#ddd}
.team-panel{position:absolute;left:200px;top:27px;width:142px;height:151px;background:var(--panel-grey);border-radius:5px;padding:12px 6px;display:flex;flex-direction:column;gap:7.4px}

/* slide 4 */
.section-mark{position:absolute;left:14px;top:57px;width:72px;height:72px;background:linear-gradient(135deg,var(--olive),var(--sky) 50%,var(--green))}
.section-title{position:absolute;left:103px;top:80px;font:800 22px/1 'Montserrat',sans-serif;color:var(--ink)}
.section-sub{position:absolute;left:104px;top:105px;font-size:6.4px;color:#222}
.section-rule{position:absolute;left:103px;right:10px;top:117.5px;height:.6px;background:#aaa}

/* slide 5 */
.chevrons{position:absolute;left:11px;top:30px}
.chev-row{position:absolute;left:65px;width:277px;height:41px;background:var(--panel);border-radius:4px;padding:6px 0 0 8px;display:flex;flex-direction:column;gap:4.2px}
.chev-label{position:absolute;left:11px;width:52px;text-align:center;font-size:6.3px;color:#fff}

/* slide 6 */
.tagline{position:absolute;left:11px;font-size:6.4px;color:var(--blue)}
.para{position:absolute;left:11px;right:10px;font-size:4.5px;line-height:1.3;color:#222}
.data-table{position:absolute;left:11px;top:103px;width:331px;height:75px;border-collapse:collapse;table-layout:fixed}
.data-table td,.data-table th{font-size:3.2px;font-weight:400;text-align:center;color:#333;border:.5px solid #fff}
.data-table .navy{background:var(--navy);color:#fff}
.data-table .hd{height:10px;font-size:4.6px}
.data-table .sub{height:16px;color:#fff;font-size:4.2px}
.data-table .r1{background:#ebe9e8}.data-table .r2{background:#f4f2f1}
.vert{writing-mode:vertical-rl;transform:rotate(180deg);font-size:4.6px}

/* slide 9 */
.deal-strip{position:absolute;left:11px;top:29px;width:331px;display:grid;grid-template-columns:1fr 1fr 1fr;gap:3px}
.deal-strip div{display:flex;justify-content:space-between;padding:0 3px;height:9px;font-size:3px;line-height:9px;color:#fff}
.deal-strip .lo{background:var(--taupe)}
.panel-light{position:absolute;background:#f4f1ee}
.panel-head{font:700 4.8px 'Lato',sans-serif;color:var(--blue)}
.sub-bullets{list-style:disc;padding-left:12px;margin:2px 0 5px;font-size:3.6px;line-height:1.45;color:#444}
.chart-box{position:absolute;width:63px;height:33px;background:var(--taupe);border-radius:5px;font:700 6px/33px 'Lato',sans-serif;color:#fff;text-align:center}

/* slide 10 */
.co-logo{position:absolute;right:32px;top:6px;width:35px;height:13px;border-radius:2px;background:var(--taupe);font-size:6px;line-height:13px;color:#fff;text-align:center}
.metrics{position:absolute;top:38px;font-size:3.6px;line-height:1.9;color:#444}
.metrics u{display:block;color:var(--blue);font-size:3.8px}
.product{position:absolute;top:30px;width:38px;height:53px;border-radius:4px;background:var(--taupe);font:700 4.6px/53px 'Lato',sans-serif;color:#fff;text-align:center}
.case-box .box-body{gap:5.5px;padding:6px 7px}
</style>
</head>
<body>

<header>
  <div class="sheet-brand"><i class="brand-square"></i><div class="brand-name">Brackwell Thorne Equity Partners</div></div>
  <div class="sheet-divider"></div>
  <h1 class="sheet-heading">POWERPOINT<br>PRESENTATION<br>TEMPLATE</h1>
</header>

<!-- 1 cover -->
<section class="slide col-l row1">
  <div class="cover-brand"><i></i><span>Brackwell Thorne Equity Partners</span></div>
  <h2 class="cover-headline">Realizing the promise in<br>small companies for decades</h2>
  <div class="values"><span class="bg-blue">PERSEVERANCE</span><span class="bg-green">INGENUITY</span><span class="bg-sky">TRANSPARENCY</span><span class="bg-olive">RESULTS</span></div>
  <div class="cover-rule"></div>
  <p class="cover-url">www.bteqx.com</p>
  <p class="cover-date">[May 2026]</p>
</section>

<!-- 2 bullets -->
<section class="slide col-r row1">
  <h2 class="slide-title">Insert Title Here</h2><div class="title-rule"></div>
  <div class="corner-mark"><i></i></div>
  <div class="two-col">
    <div class="bl"><b>[Bullet]</b><span>Lorem ipsum dolor sit amet consectetur adipiscing elit.</span></div>
    <div class="bl"><b>[Bullet]</b><span>Lorem ipsum dolor sit amet consectetur adipiscing elit.</span></div>
    <div class="bl"><b>[Bullet]</b><span>Lorem ipsum dolor sit amet consectetur adipiscing elit.</span></div>
    <div class="bl"><b>[Bullet]</b><span>Lorem ipsum dolor sit amet consectetur adipiscing elit.</span></div>
    <div class="bl"><b>[Bullet]</b><span>Lorem ipsum dolor sit amet consectetur adipiscing elit.</span></div>
    <div class="bl"><b>[Bullet]</b><span>Lorem ipsum dolor sit amet consectetur adipiscing elit.</span></div>
    <div class="bl"><b>[Bullet]</b><span>Lorem ipsum dolor sit amet consectetur adipiscing elit.</span></div>
    <div class="bl"><b>[Bullet]</b><span>Lorem ipsum dolor sit amet consectetur adipiscing elit.</span></div>
    <div class="bl"><b>[Bullet]</b><span>Lorem ipsum dolor sit amet consectetur adipiscing elit.</span></div>
    <div class="bl"><b>[Bullet]</b><span>Lorem ipsum dolor sit amet consectetur adipiscing elit.</span></div>
    <div class="bl"><b>[Bullet]</b><span>Lorem ipsum dolor sit amet consectetur adipiscing elit.</span></div>
    <div class="bl"><b>[Bullet]</b><span>Lorem ipsum dolor sit amet consectetur adipiscing elit.</span></div>
  </div>
  <p class="foot foot-l">Brackwell Thorne Equity Partners | Confidential</p><p class="foot foot-r">www.bteqx.com &nbsp;| &nbsp;2</p>
</section>

<!-- 3 team -->
<section class="slide col-l row2">
  <h2 class="slide-title">Team</h2><div class="title-rule"></div>
  <div class="corner-mark"><i></i></div>
  <div class="team-bar bg-blue" style="top:27px">[Section]</div>
  <div class="team-grid" style="top:45px">
    <div class="member"><div class="foto">Foto</div>[Name]<br>[Year]</div>
    <div class="member"><div class="foto">Foto</div>[Name]<br>[Year]</div>
    <div class="member"><div class="foto">Foto</div>[Name]<br>[Year]</div>
    <div class="member"><div class="foto">Foto</div>[Name]<br>[Year]</div>
    <div class="member"><div class="foto">Foto</div>[Name]<br>[Year]</div>
    <div class="member"><div class="foto">Foto</div>[Name]<br>[Year]</div>
  </div>
  <div class="team-bar bg-green" style="top:121px">[Section]</div>
  <div class="team-grid" style="top:139px">
    <div class="member"><div class="foto">Foto</div>[Name]<br>[Title]<br>[Year]</div>
    <div class="member"><div class="foto">Foto</div>[Name]<br>[Title]<br>[Year]</div>
    <div class="member"><div class="foto">Foto</div>[Name]<br>[Title]<br>[Year]</div>
  </div>
  <div class="team-panel">
    <div class="bl"><b>[Bullet]</b><span>Lorem ipsum dolor sit amet consectetur adipiscing elit.</span></div>
    <div class="bl"><b>[Bullet]</b><span>Lorem ipsum dolor sit amet consectetur adipiscing elit.</span></div>
    <div class="bl"><b>[Bullet]</b><span>Lorem ipsum dolor sit amet consectetur adipiscing elit.</span></div>
    <div class="bl"><b>[Bullet]</b><span>Lorem ipsum dolor sit amet consectetur adipiscing elit.</span></div>
    <div class="bl"><b>[Bullet]</b><span>Lorem ipsum dolor sit amet consectetur adipiscing elit.</span></div>
    <div class="bl"><b>[Bullet]</b><span>Lorem ipsum dolor sit amet consectetur adipiscing elit.</span></div>
  </div>
  <p class="footnote" style="bottom:14px">Footnote</p>
  <p class="foot foot-l">Brackwell Thorne Equity Partners | Confidential</p><p class="foot foot-r">www.bteqx.com &nbsp;| &nbsp;3</p>
</section>

<!-- 4 section divider -->
<section class="slide col-r row2">
  <div class="section-mark" role="img" aria-label="Brand colour block"></div>
  <h2 class="section-title">NEW SECTION</h2>
  <p class="section-sub">Lorem ipsum dolor sit amet consectetur adipiscing elit.</p>
  <div class="section-rule"></div>
</section>

<!-- 5 chevron process -->
<section class="slide col-l row3">
  <h2 class="slide-title">Insert Title Here</h2><div class="title-rule"></div>
  <div class="corner-mark"><i></i></div>
  <svg class="chevrons" width="52" height="146" viewBox="0 0 52 146">
    <polygon points="0,0 52,0 52,38 26,52 0,38" fill="#2f6d9c"/>
    <polygon points="0,46 26,59 52,46 52,84 26,98 0,84" fill="#337d55"/>
    <polygon points="0,91 26,104 52,91 52,129 26,146 0,129" fill="#b7a532"/>
  </svg>
  <span class="chev-label" style="top:50px">[Insert Text]</span>
  <span class="chev-label" style="top:95px">[Insert Text]</span>
  <span class="chev-label" style="top:140px">[Insert Text]</span>
  <div class="chev-row" style="top:30px">
    <p class="line">Lorem ipsum dolor sit amet consectetur adipiscing elit. Quisque faucibus ex sapien vitae pellentesque sem.</p>
    <p class="line">Lorem ipsum dolor sit amet consectetur adipiscing elit. Quisque faucibus ex sapien vitae pellentesque sem.</p>
    <p class="line">Lorem ipsum dolor sit amet consectetur adipiscing elit. Quisque faucibus ex sapien vitae pellentesque sem.</p>
  </div>
  <div class="chev-row" style="top:75px">
    <p class="line">Lorem ipsum dolor sit amet consectetur adipiscing elit. Quisque faucibus ex sapien vitae pellentesque sem.</p>
    <p class="line">Lorem ipsum dolor sit amet consectetur adipiscing elit. Quisque faucibus ex sapien vitae pellentesque sem.</p>
    <p class="line">Lorem ipsum dolor sit amet consectetur adipiscing elit. Quisque faucibus ex sapien vitae pellentesque sem.</p>
  </div>
  <div class="chev-row" style="top:120px">
    <p class="line">Lorem ipsum dolor sit amet consectetur adipiscing elit. Quisque faucibus ex sapien vitae pellentesque sem.</p>
    <p class="line">Lorem ipsum dolor sit amet consectetur adipiscing elit. Quisque faucibus ex sapien vitae pellentesque sem.</p>
    <p class="line">Lorem ipsum dolor sit amet consectetur adipiscing elit. Quisque faucibus ex sapien vitae pellentesque sem.</p>
  </div>
  <p class="foot foot-l">Brackwell Thorne Equity Partners | Confidential</p><p class="foot foot-r">www.bteqx.com &nbsp;| &nbsp;5</p>
</section>

<!-- 6 text + table -->
<section class="slide col-r row3">
  <h2 class="slide-title">Insert Title Here</h2><div class="title-rule"></div>
  <div class="corner-mark"><i></i></div>
  <p class="tagline" style="top:29px">[Tagline]</p>
  <p class="para" style="top:42px">Lorem ipsum dolor sit amet consectetur adipiscing elit. Quisque faucibus ex sapien vitae pellentesque sem placerat. In id cursus mi pretium tellus duis convallis. Tempus leo eu aenean sed diam urna tempor. Pulvinar vivamus fringilla lacus nec metus bibendum egestas. Iaculis massa nisl malesuada lacinia integer nunc posuere. Ut hendrerit semper vel class aptent taciti sociosqu.</p>
  <p class="para" style="top:69px">Lorem ipsum dolor sit amet consectetur adipiscing elit. Quisque faucibus ex sapien vitae pellentesque sem placerat. In id cursus mi pretium tellus duis convallis. Tempus leo eu aenean sed diam urna tempor. Pulvinar vivamus fringilla lacus nec metus bibendum egestas. Iaculis massa nisl malesuada lacinia integer nunc posuere. Ut hendrerit semper vel class aptent taciti sociosqu.</p>
  <table class="data-table">
    <colgroup><col style="width:21px"><col><col><col><col><col><col></colgroup>
    <tr><td class="navy" rowspan="2"></td><th class="navy hd" colspan="6">[Title]</th></tr>
    <tr><th class="sub bg-sky" colspan="2">[Sub section]</th><th class="sub bg-green" colspan="2">[Sub section]</th><th class="sub bg-olive" colspan="2">[Sub section]</th></tr>
    <tr class="r1"><td class="navy" rowspan="4"><span class="vert">[Title]</span></td><td>LOGO</td><td>[Description]</td><td>LOGO</td><td>[Description]</td><td>LOGO</td><td>[Description]</td></tr>
    <tr class="r2"><td>LOGO</td><td>[Description]</td><td>LOGO</td><td>[Description]</td><td>LOGO</td><td>[Description]</td></tr>
    <tr class="r1"><td>LOGO</td><td>[Description]</td><td>LOGO</td><td>[Description]</td><td>LOGO</td><td>[Description]</td></tr>
    <tr class="r2"><td>LOGO</td><td>[Description]</td><td>LOGO</td><td>[Description]</td><td>LOGO</td><td>[Description]</td></tr>
  </table>
  <p class="foot foot-l">Brackwell Thorne Equity Partners | Confidential</p><p class="foot foot-r">www.bteqx.com &nbsp;| &nbsp;6</p>
</section>

<!-- 7 three sections -->
<section class="slide col-l row4">
  <h2 class="slide-title">Insert Title Here</h2><div class="title-rule"></div>
  <div class="corner-mark"><i></i></div>
  <div class="box" style="left:11px;top:32px;width:159px;height:146px">
    <div class="box-head bg-blue">[Section]</div>
    <div class="box-body">
      <div class="bl"><b>[Bullet]</b><span>Lorem ipsum dolor sit amet consectetur adipiscing elit.</span></div>
      <div class="bl"><b>[Bullet]</b><span>Lorem ipsum dolor sit amet consectetur adipiscing elit.</span></div>
      <div class="bl"><b>[Bullet]</b><span>Lorem ipsum dolor sit amet consectetur adipiscing elit.</span></div>
      <div class="bl"><b>[Bullet]</b><span>Lorem ipsum dolor sit amet consectetur adipiscing elit.</span></div>
      <div class="bl"><b>[Bullet]</b><span>Lorem ipsum dolor sit amet consectetur adipiscing elit.</span></div>
      <div class="bl"><b>[Bullet]</b><span>Lorem ipsum dolor sit amet consectetur adipiscing elit.</span></div>
    </div>
  </div>
  <div class="box" style="left:182px;top:32px;width:160px;height:70px">
    <div class="box-head bg-green">[Section]</div>
    <div class="box-body">
      <div class="bl"><b>[Bullet]</b><span>Lorem ipsum dolor sit amet consectetur adipiscing elit.</span></div>
      <div class="bl"><b>[Bullet]</b><span>Lorem ipsum dolor sit amet consectetur adipiscing elit.</span></div>
    </div>
  </div>
  <div class="box" style="left:182px;top:109px;width:160px;height:69px">
    <div class="box-head bg-olive">[Section]</div>
    <div class="box-body">
      <div class="bl"><b>[Bullet]</b><span>Lorem ipsum dolor sit amet consectetur adipiscing elit.</span></div>
      <div class="bl"><b>[Bullet]</b><span>Lorem ipsum dolor sit amet consectetur adipiscing elit.</span></div>
    </div>
  </div>
  <p class="foot foot-l">Brackwell Thorne Equity Partners | Confidential</p><p class="foot foot-r">www.bteqx.com &nbsp;| &nbsp;7</p>
</section>

<!-- 8 four sections -->
<section class="slide col-r row4">
  <h2 class="slide-title">Insert Title Here</h2><div class="title-rule"></div>
  <div class="corner-mark"><i></i></div>
  <p class="tagline" style="top:27px">[Tagline]</p>
  <div class="box" style="left:11px;top:37px;width:159px;height:70px">
    <div class="box-head bg-blue">[Section]</div>
    <div class="box-body">
      <div class="bl"><b>[Bullet]</b><span>Lorem ipsum dolor sit amet consectetur adipiscing elit.</span></div>
      <div class="bl"><b>[Bullet]</b><span>Lorem ipsum dolor sit amet consectetur adipiscing elit.</span></div>
    </div>
  </div>
  <div class="box" style="left:182px;top:37px;width:160px;height:70px">
    <div class="box-head bg-green">[Section]</div>
    <div class="box-body">
      <div class="bl"><b>[Bullet]</b><span>Lorem ipsum dolor sit amet consectetur adipiscing elit.</span></div>
      <div class="bl"><b>[Bullet]</b><span>Lorem ipsum dolor sit amet consectetur adipiscing elit.</span></div>
    </div>
  </div>
  <div class="box" style="left:11px;top:114px;width:159px;height:70px">
    <div class="box-head bg-sky">[Section]</div>
    <div class="box-body">
      <div class="bl"><b>[Bullet]</b><span>Lorem ipsum dolor sit amet consectetur adipiscing elit.</span></div>
      <div class="bl"><b>[Bullet]</b><span>Lorem ipsum dolor sit amet consectetur adipiscing elit.</span></div>
    </div>
  </div>
  <div class="box" style="left:182px;top:114px;width:160px;height:70px">
    <div class="box-head bg-olive">[Section]</div>
    <div class="box-body">
      <div class="bl"><b>[Bullet]</b><span>Lorem ipsum dolor sit amet consectetur adipiscing elit.</span></div>
      <div class="bl"><b>[Bullet]</b><span>Lorem ipsum dolor sit amet consectetur adipiscing elit.</span></div>
    </div>
  </div>
  <p class="foot foot-l">Brackwell Thorne Equity Partners | Confidential</p><p class="foot foot-r">www.bteqx.com &nbsp;| &nbsp;8</p>
</section>

<!-- 9 deal summary -->
<section class="slide col-l row5">
  <h2 class="slide-title">Insert Title Here</h2><div class="title-rule"></div>
  <div class="corner-mark"><i></i></div>
  <div class="deal-strip">
    <div class="bg-blue"><span>Source:</span><span>[Investment Bank, Auction Sale Process]</span></div>
    <div class="bg-green"><span>Investment Dates:</span><span>[ ] to [ ]</span></div>
    <div class="bg-olive"><span>Fund Investment:</span><span>$X.X million</span></div>
    <div class="lo"><span>Enterprise Value @ Entry:</span><span>$XX million</span></div>
    <div class="lo"><span>Enterprise Value @ Exit:</span><span>$XXX million</span></div>
    <div class="lo"><span>Co-Investment:</span><span>$X.X million</span></div>
  </div>
  <div class="panel-light" style="left:11px;top:50px;width:163px;height:122px;padding:6px 4px">
    <p class="line panel-head" style="font-size:4.8px">[Company] Description</p>
    <ul class="sub-bullets"><li>Lorem ipsum dolor sit amet consectetur adipiscing elit.</li><li>Lorem ipsum dolor sit amet consectetur adipiscing elit.</li><li>Lorem ipsum dolor sit amet consectetur adipiscing elit.</li><li>Lorem ipsum dolor sit amet consectetur adipiscing elit.</li></ul>
    <p class="line panel-head" style="font-size:4.8px">Investment Thesis</p>
    <ul class="sub-bullets"><li>Lorem ipsum dolor sit amet consectetur adipiscing elit.</li><li>Lorem ipsum dolor sit amet consectetur adipiscing elit.</li><li>Lorem ipsum dolor sit amet consectetur adipiscing elit.</li><li>Lorem ipsum dolor sit amet consectetur adipiscing elit.</li></ul>
    <p class="line panel-head" style="font-size:4.8px">Value Creation</p>
    <ul class="sub-bullets"><li>Lorem ipsum dolor sit amet consectetur adipiscing elit.</li><li>Lorem ipsum dolor sit amet consectetur adipiscing elit.</li><li>Lorem ipsum dolor sit amet consectetur adipiscing elit.</li><li>Lorem ipsum dolor sit amet consectetur adipiscing elit.</li></ul>
  </div>
  <div class="panel-light" style="left:177px;top:50px;width:165px;height:64px;padding:6px 5px">
    <p class="panel-head">Financial Profile</p>
    <p style="position:absolute;left:78px;top:17px;font-size:3.8px;color:#444">[xxxxxxx]:</p>
    <ul class="sub-bullets" style="position:absolute;left:78px;top:22px;width:84px"><li>Lorem ipsum dolor sit amet consectetur</li><li>Lorem ipsum dolor sit amet consectetur</li><li>Lorem ipsum dolor sit amet consectetur</li><li>Lorem ipsum dolor sit amet consectetur</li></ul>
  </div>
  <div class="chart-box" style="left:182px;top:69px">Bar Chart</div>
  <div class="panel-light" style="left:177px;top:119px;width:165px;height:53px;padding:6px 5px">
    <p class="panel-head">Investment Performance</p>
    <p style="position:absolute;left:100px;top:26px;font-size:3.8px;line-height:1.2;text-align:center;color:#333">##% Gross<br>IRR</p>
  </div>
  <div class="chart-box" style="left:182px;top:136px">Bar Chart</div>
  <p class="footnote" style="bottom:13px">Footnote</p>
  <p class="foot foot-l">Brackwell Thorne Equity Partners | Confidential</p><p class="foot foot-r">www.bteqx.com &nbsp;| &nbsp;9</p>
</section>

<!-- 10 case study -->
<section class="slide col-r row5">
  <h2 class="slide-title">[PortCo Case Study]</h2><div class="title-rule"></div>
  <div class="co-logo">Co.Logo</div>
  <div class="corner-mark"><i></i></div>
  <p class="tagline" style="top:26px">[Tagline]</p>
  <div class="metrics" style="left:11px">
    <u>Closing Metrics</u>
    <p class="line" style="font-size:3.6px">Investment Date: &nbsp;[Xxxx]</p>
    <p class="line" style="font-size:3.6px">Enterprise Value: &nbsp;$##.# million</p>
    <p class="line" style="font-size:3.6px">EBITDA Multiple: &nbsp;#.#x</p>
    <p class="line" style="font-size:3.6px">Fund Investment: &nbsp;$##.# million</p>
    <p class="line" style="font-size:3.6px">Co-investment: &nbsp;&nbsp;$##.# million</p>
  </div>
  <div class="metrics" style="left:92px">
    <u>Current Metrics ([Date])</u>
    <p class="line" style="font-size:3.6px">Enterprise Value: &nbsp;&nbsp;$##.# million</p>
    <p class="line" style="font-size:3.6px">TVPI: &nbsp;&nbsp;&nbsp;&nbsp;&nbsp;&nbsp;&nbsp;&nbsp;&nbsp;&nbsp;&nbsp;&nbsp;&nbsp;&nbsp;&nbsp;#.#x</p>
    <p class="line" style="font-size:3.6px">EBITDA Multiple: &nbsp;&nbsp;&nbsp;#.#x</p>
    <p class="line" style="font-size:3.6px">Mgmt. Investors: &nbsp;&nbsp;##</p>
    <p class="line" style="font-size:3.6px">Add-on Acquisitions: ##</p>
  </div>
  <div class="product" style="left:171px" role="img" aria-label="Product photo placeholder">Product Pic</div>
  <div class="product" style="left:214px" role="img" aria-label="Product photo placeholder">Product Pic</div>
  <div class="product" style="left:258px" role="img" aria-label="Product photo placeholder">Product Pic</div>
  <div class="product" style="left:301px;width:41px" role="img" aria-label="Product photo placeholder">Product Pic</div>
  <div class="box case-box" style="left:11px;top:91px;width:105px;height:86px">
    <div class="box-head bg-blue">[Section]</div>
    <div class="box-body"><p class="line">Lorem ipsum dolor sit amet.</p><p class="line">Lorem ipsum dolor sit amet.</p><p class="line">Lorem ipsum dolor sit amet.</p><p class="line">Lorem ipsum dolor sit amet.</p><p class="line">Lorem ipsum dolor sit amet.</p><p class="line">Lorem ipsum dolor sit amet.</p></div>
  </div>
  <div class="box case-box" style="left:124px;top:91px;width:105px;height:86px">
    <div class="box-head bg-green">[Section]</div>
    <div class="box-body"><p class="line">Lorem ipsum dolor sit amet.</p><p class="line">Lorem ipsum dolor sit amet.</p><p class="line">Lorem ipsum dolor sit amet.</p><p class="line">Lorem ipsum dolor sit amet.</p><p class="line">Lorem ipsum dolor sit amet.</p><p class="line">Lorem ipsum dolor sit amet.</p></div>
  </div>
  <div class="box case-box" style="left:237px;top:91px;width:105px;height:86px">
    <div class="box-head bg-olive">[Section]</div>
    <div class="box-body"><p class="line">Lorem ipsum dolor sit amet.</p><p class="line">Lorem ipsum dolor sit amet.</p><p class="line">Lorem ipsum dolor sit amet.</p><p class="line">Lorem ipsum dolor sit amet.</p><p class="line">Lorem ipsum dolor sit amet.</p><p class="line">Lorem ipsum dolor sit amet.</p></div>
  </div>
  <p class="footnote" style="bottom:13px">Footnote</p>
  <p class="foot foot-l">Brackwell Thorne Equity Partners | Confidential</p><p class="foot foot-r">www.bteqx.com &nbsp;| &nbsp;10</p>
</section>

</body>
</html>
```